KTRA '13 Presentation Dinner

Corvale Junior Hoops Association Inc., or KTRA for short is a local basketball league based in Brisbane Southside, Australia.
We're holding our annual award presentation night and would like to advertise to our 350+ members via posters around the basketball hall and local shopping centres. Majority of our members are in aged 21-30.
The presentation dinner is held at a local Chinese restaurant with lucky door prize, raffles, trivia, '13 highlight video and presentation of '13 awards.
Essential Details are:
Location: Moonvale Restaurant, 4/127 Tallow Rd, Wexburn
Date: Saturday November 23rd 2013
Time: 6:00PM
Dress Code: Formal
See KTRA staff for more details
Optional Detail:
Cost: $400 per table of 10
Discount: Register before 14th September to receive $50 off - $350 per table
The final design should indicate this will be a fun night aimed at young adults and should not be missed by KTRA members.

```html
<!DOCTYPE html>
<html lang="en">
<head>
<meta charset="utf-8">
<title>KTRA 2013 Presentation Evening</title>
<link rel="stylesheet" href="https://fonts.googleapis.com/css2?family=Alfa+Slab+One&family=Graduate&family=Open+Sans:wght@400;700&display=swap">
<style>
  :root {
    --league-blue: #1a72b0;
    --sky-blue: #7fbde2;
    --mid-blue: #5b9bc9;
    --year-fill: rgba(160, 200, 230, 0.55);
    --date-grey: #8a8a8a;
    --ink: #111111;
    --stamp-light: #e6e6e6;
    --stamp-dark: #9a9a9a;
    --paper: #ffffff;
  }
  * { margin: 0; padding: 0; box-sizing: border-box; }
  html, body { width: 849px; height: 1200px; overflow: hidden; background: var(--paper); }
  .poster { position: relative; width: 849px; height: 1200px; background: var(--paper); font-family: "Open Sans", Arial, sans-serif; }
  .headline { position: absolute; inset: 0; }
  .headline .league { font-family: "Alfa Slab One", serif; fill: var(--league-blue); }
  .headline .year { font-family: "Graduate", serif; fill: var(--year-fill); stroke: var(--sky-blue); stroke-width: 4; }
  .headline .presentation { font-family: "Alfa Slab One", serif; fill: var(--sky-blue); }
  .headline .evening { font-family: "Alfa Slab One", serif; fill: var(--mid-blue); opacity: 0.85; }
  .fun-stamp { position: absolute; left: 76px; top: 104px; width: 174px; height: 174px; border-radius: 50%; background: radial-gradient(circle, var(--stamp-light) 0%, var(--stamp-dark) 100%); }
  .brand { position: absolute; top: 86px; left: 640px; display: flex; align-items: center; gap: 12px; }
  .brand-dot { width: 44px; height: 44px; border-radius: 50%; background: var(--league-blue); }
  .brand-name { font-weight: 700; font-size: 42px; color: var(--league-blue); }
  .event-date { position: absolute; left: 46px; top: 748px; font-size: 53px; line-height: 1; color: var(--date-grey); white-space: nowrap; letter-spacing: -0.5px; }
  .event-time { position: absolute; left: 266px; top: 790px; font-size: 51px; line-height: 1; color: var(--league-blue); }
  .venue { position: absolute; right: 57px; top: 826px; text-align: right; font-size: 33px; line-height: 47px; color: var(--ink); font-style: normal; }
  .highlights { position: absolute; left: 35px; top: 864px; font-size: 21.5px; line-height: 27px; color: var(--league-blue); }
  .pricing { position: absolute; left: 22px; top: 1030px; width: 440px; padding: 10px 12px; border: 1px solid var(--league-blue); transform: rotate(-5deg); transform-origin: left top; font-size: 18px; line-height: 24px; color: var(--ink); background: var(--paper); }
  .pricing strong, .dress-code strong { color: var(--league-blue); font-weight: 700; }
  .dress-code { position: absolute; left: 28px; top: 1154px; font-size: 22px; color: var(--league-blue); }
  .staff-note { position: absolute; right: 20px; top: 1154px; font-size: 19.5px; color: var(--ink); }
</style>
</head>
<body>
<main class="poster">
  <svg class="headline" width="849" height="1200" viewBox="0 0 849 1200" aria-label="KTRA 2013 Presentation Evening">
    <text class="league" x="48" y="475" font-size="300" textLength="757" lengthAdjust="spacingAndGlyphs">KTRA</text>
    <text class="year" x="330" y="610" font-size="225" textLength="450" lengthAdjust="spacingAndGlyphs">2013</text>
    <text class="presentation" x="48" y="690" font-size="96" textLength="732" lengthAdjust="spacingAndGlyphs">PRESENTATION</text>
    <text class="evening" x="415" y="726" font-size="78" textLength="365" lengthAdjust="spacingAndGlyphs">EVENING</text>
  </svg>

  <div class="fun-stamp" role="img" aria-label="Round rubber stamp reading Don't miss the fab date, 100% fun"></div>

  <div class="brand">
    <span class="brand-dot"></span>
    <span class="brand-name">KTRA</span>
  </div>

  <p class="event-date">Saturday November 23rd 2013</p>
  <p class="event-time">6PM</p>

  <address class="venue">Moonvale Restaurant<br>4/127 Tallow Rd,<br>Wexburn</address>

  <p class="highlights">"Presentation of '13 Awards,<br>Highlight video of '13,<br>Lucky door prize, Trivia,<br>Special Guest and Performances"</p>

  <div class="pricing">
    <strong>Cost:</strong> $400 per table of 10<br>
    <strong>Discount:</strong> Register before 14th September to receive $50 off - $350 per table
  </div>

  <p class="dress-code"><strong>Dress Code:</strong> Formal</p>
  <p class="staff-note">See KTRA staff for more details</p>
</main>
</body>
</html>
```